Naturkosmetikpraxis sucht Design
Der Designer konnte gut meine Vorstellungen umsetzen und das in kürzester Zeit. Eine super Leistung, vor allem da ich weiß, dass es mir oft schwerfällt, mich klar auszudrücken.
Zielgruppe
Kosmetikpraxis, alle Altersgruppen aber Fokus Best Ager, vorwiegend weiblich, naturverbundene Menschen, gesundheitsbewusste Menschen, gestresste
gefallen soll es Menschen mit Hautproblemen und welchen, die einfach entspannen möchten.
Menschen, die Individualität suchen - nicht preiswerte Masse.
Aufgabenstellung
natürliche Hautpflegekonzepte,
Sugaring-Enthaarung, Wellness-Massagen, Naturnagelpflege, Wimpernlifting, Micro-Needling mit Lifting Pen, Klangschalenmassage, Permanent MakeUp
- Text mit Öffnungszeiten im Anhang "Banner..."
Als Farbe mag ich sehr dunkles rot, geht aber auch als Hintergrundfarbe. Ist wohl Brombeer etwa r171, g22, b78. Es geht ja hier um einen Banner für das Hoftor als Holz an einem Fachwerkhaus.
Habe noch ein paar Fotos aus meinem Bestand beigefügt.
Anderes Bild natürlich auch o.k.
BILD: 48193527 Frau m. Freesie von Bildarix. Das anhängende Bild flieder bluete 71846302 geht in eine ganz andere Richtung, ich weiß. Aber es ist ein tolles Bild und ich wäre durchaus bereit, auf flieder im Design zu wechseln. 08.04.14: jetzt hat sich das LOGO doch verändert.

```html
<!DOCTYPE html>
<html lang="de">
<head>
<meta charset="utf-8">
<title>Helena Brandauer Kosmetikpraxis – Banner</title>
<link rel="stylesheet" href="https://fonts.googleapis.com/css2?family=Arimo:wght@400&display=swap">
<style>
  :root {
    --brand-red: #8c1b1f;
    --silver-light: #f4f4f4;
    --silver-mid: #d2d2d2;
    --silver-dark: #a9a9a9;
    --blush: #efc2c8;
    --blush-soft: #fbeef0;
    --skin-light: #f7e6de;
    --skin: #ecc9b8;
    --skin-deep: #dfae9a;
    --url-text: #4a4a4a;
    --white: #ffffff;
  }
  html, body {
    margin: 0;
    padding: 0;
    width: 1200px;
    height: 2519px;
    overflow: hidden;
    background: var(--white);
  }
  .banner {
    position: relative;
    width: 1200px;
    height: 2519px;
    overflow: hidden;
    font-family: "Arimo", Arial, sans-serif;
    background: var(--white);
  }
  .masthead {
    position: absolute;
    left: 0; top: 0;
    width: 1200px; height: 330px;
    background: linear-gradient(90deg, var(--silver-dark) 0%, var(--silver-light) 30%, var(--white) 50%, var(--silver-light) 70%, var(--silver-dark) 100%);
    text-align: center;
    color: var(--brand-red);
  }
  .masthead__name {
    margin: 0;
    padding-top: 38px;
    font-size: 112px;
    font-weight: 400;
    line-height: 1.1;
    letter-spacing: -1px;
  }
  .masthead__tagline {
    margin: 4px 0 0;
    font-size: 68px;
    font-weight: 400;
    line-height: 1.1;
  }
  .hero {
    position: absolute;
    left: 0; top: 330px;
    width: 1200px; height: 1250px;
    background:
      radial-gradient(ellipse 560px 700px at 620px 560px, var(--skin) 0%, var(--skin-light) 60%, rgba(247,230,222,0) 100%),
      radial-gradient(ellipse 420px 360px at 330px 1080px, var(--skin-deep) 0%, rgba(223,174,154,0) 100%),
      linear-gradient(135deg, var(--skin-light) 0%, var(--blush-soft) 45%, var(--blush) 100%);
  }
  .content {
    position: absolute;
    left: 0; top: 1560px;
    width: 1200px; height: 580px;
    background: linear-gradient(180deg, #f8f8f8 0%, #ececec 100%);
  }
  .swoosh {
    position: absolute;
    left: 0; top: 1440px;
    width: 1200px; height: 130px;
  }
  .services {
    position: absolute;
    left: 0; top: 1612px;
    width: 1200px;
    margin: 0; padding: 0;
    list-style: none;
    text-align: center;
    color: var(--brand-red);
    font-size: 60px;
    line-height: 81px;
  }
  .web-bar {
    position: absolute;
    left: 0; top: 2140px;
    width: 1200px; height: 78px;
    background: linear-gradient(90deg, var(--silver-light) 0%, var(--white) 40%, var(--blush-soft) 70%, #e99aa3 100%);
    color: var(--url-text);
    font-size: 52px;
    line-height: 78px;
    text-align: center;
  }
  .footer {
    position: absolute;
    left: 0; top: 2218px;
    width: 1200px; height: 301px;
    background: linear-gradient(90deg, var(--silver-dark) 0%, var(--silver-mid) 30%, var(--silver-light) 50%, var(--silver-mid) 70%, var(--silver-dark) 100%);
    display: flex;
    align-items: center;
    justify-content: center;
    gap: 30px;
  }
  .footer__mark {
    width: 60px; height: 60px;
    border-radius: 50%;
    border: 5px solid var(--white);
    box-sizing: border-box;
  }
  .footer__name {
    color: var(--white);
    font-size: 96px;
    font-weight: 400;
  }
</style>
</head>
<body>
  <div class="banner">
    <header class="masthead">
      <h1 class="masthead__name">Helena Brandauer</h1>
      <p class="masthead__tagline">Kosmetikpraxis</p>
    </header>

    <div class="hero" role="img" aria-label="Foto einer entspannten Frau mit geschlossenen Augen, die Hand am Hals, vor zartrosa Hintergrund"></div>

    <div class="content"></div>

    <svg class="swoosh" viewBox="0 0 1200 130" preserveAspectRatio="none" aria-hidden="true">
      <path d="M0 80 C 350 10, 850 0, 1200 60 L1200 130 L0 130 Z" fill="#f8f8f8"/>
      <path d="M480 110 C 750 70, 1000 60, 1200 80" fill="none" stroke="#f2d4d8" stroke-width="6"/>
    </svg>

    <ul class="services">
      <li>Natürliche Hautpflege</li>
      <li>Sugaring-Enthaarung</li>
      <li>Wellnessmassagen</li>
      <li>Maniküre</li>
      <li>Wimpernlifting</li>
      <li>Permanent Make-Up</li>
    </ul>

    <div class="web-bar">www.kosmetikstudio-brandauer.de</div>

    <footer class="footer">
      <span class="footer__mark" aria-hidden="true"></span>
      <span class="footer__name">Lumenta</span>
    </footer>
  </div>
</body>
</html>
```